Bloom Where You Stand redesign book cover

A new cover for my already published book. The old cover looks great but not for a women’s self help book. Cover is killing sales. Once I explain the book it sells quickly AND gets 5 star reviews. Outside of actually explaining the book the cover scares people away. I need a new cover. ASAP! Before The yr end please.
The tag line -
Discover 10 Practical Ways To Replace negative thoughts with knowing the voice of God. This is a self help book for women 35-45 Christian but not religious. Each chapter is a hands on spiritual experience where the reader takes small tests about themselves, discover why they have negative thoughts, what they are and how to listen to God through hands on methods of listening. NOT strange type of things. They learn what 4 voices they are listening to and how to hone in on Jesus voice. There are scriptures to pray and journaling assignments. The old cover is in the brief with the write up for the back of the book. Please use the new author picture, Publishers logo (tree), barcode, and contact info from the back of the book. And yes the author name and title of the book on the spine. Lay out on the back cover needs to be interesting. You have all the info have fun with it.

Target Market(s)

Women 35-45 yrs old Christian and new believers or seekers.

Industry/Entity Type

Non profit organization. Missionary

Requirements
Must have
• Something DIFFERENT than what is there now. Something inviting. Fresh clear title
Nice to have
• Multi colors however a white stand out cover is also good.
Should not have
• Heavy religious feeling. No church steeples, Jesus faces.

```html
<!DOCTYPE html>
<html lang="en">
<head>
<meta charset="utf-8">
<title>Bloom Where You Stand – Cover Wrap</title>
<link href="https://fonts.googleapis.com/css2?family=Poppins:ital,wght@1,800;1,900&family=Montserrat:wght@800;900&family=Open+Sans:wght@400&family=Mrs+Saint+Delafield&display=swap" rel="stylesheet">
<style>
  :root {
    --paper: #ffffff;
    --ink: #1c1c1c;
    --glitch-red: #ff1f1f;
    --glitch-cyan: #14ffff;
    --script-red: #e8231d;
  }
  * { margin: 0; padding: 0; box-sizing: border-box; }
  html, body { width: 1200px; height: 819px; overflow: hidden; background: var(--paper); }
  .wrap { position: relative; width: 1200px; height: 819px; overflow: hidden; background: var(--paper); color: var(--ink); }

  .glitch { text-shadow: -6px 0 var(--glitch-red), 6px 2px var(--glitch-cyan); }
  .glitch-sm { text-shadow: -3px 0 var(--glitch-red), 3px 1px var(--glitch-cyan); }
  .word-italic { font-family: "Poppins", sans-serif; font-style: italic; font-weight: 900; letter-spacing: -0.04em; line-height: 0.9; }
  .word-block { font-family: "Montserrat", sans-serif; font-weight: 900; line-height: 0.9; letter-spacing: -0.01em; }
  .word-script { font-family: "Mrs Saint Delafield", cursive; color: var(--script-red); font-weight: 400; line-height: 1; }

  /* Back cover */
  .back { position: absolute; left: 0; top: 0; width: 555px; height: 819px; }
  .back-title { position: absolute; left: 75px; top: 72px; width: 400px; text-align: center; }
  .back-title .word-italic { font-size: 84px; display: block; }
  .back-title .line-two { display: flex; align-items: baseline; justify-content: center; gap: 8px; margin-top: 2px; }
  .back-title .word-script { font-size: 46px; }
  .back-title .word-block { font-size: 62px; }
  .blurb { position: absolute; left: 53px; top: 256px; width: 444px; font-family: "Open Sans", sans-serif; font-size: 14.2px; line-height: 19.1px; text-align: justify; text-align-last: center; color: var(--ink); }
  .blurb p + p { margin-top: 19px; }

  /* Spine */
  .spine { position: absolute; left: 562px; top: 44px; width: 80px; height: 751px; display: flex; justify-content: center; }
  .spine-text { writing-mode: vertical-rl; height: 751px; display: flex; align-items: center; gap: 12px; white-space: nowrap; }
  .spine .word-italic { font-size: 52px; }
  .spine .word-script { font-size: 30px; }
  .spine .word-block { font-size: 44px; }
  .spine .spine-author { font-family: "Montserrat", sans-serif; font-weight: 900; font-size: 27px; margin-top: auto; letter-spacing: 0; }

  /* Front cover */
  .front { position: absolute; left: 690px; top: 0; width: 510px; height: 819px; }
  .front-title { position: absolute; left: 20px; top: 190px; width: 470px; text-align: center; }
  .front-title .word-italic { font-size: 116px; display: block; }
  .front-title .word-script { font-size: 84px; display: block; margin-top: 6px; }
  .front-title .word-block { font-size: 100px; display: block; margin-top: -16px; }
  .tagline { position: absolute; left: 0; top: 604px; width: 490px; text-align: center; font-family: "Poppins", sans-serif; font-style: italic; font-weight: 800; font-size: 17.5px; line-height: 20.5px; text-transform: uppercase; letter-spacing: -0.01em; }
  .author { position: absolute; left: 10px; top: 712px; width: 480px; text-align: center; font-family: "Montserrat", sans-serif; font-weight: 900; font-size: 56px; letter-spacing: -0.01em; white-space: nowrap; }
</style>
</head>
<body>
<main class="wrap">
  <section class="back">
    <h2 class="back-title">
      <span class="word-italic glitch-sm">BLOOM</span>
      <span class="line-two">
        <span class="word-script">where you</span>
        <span class="word-block">STAND</span>
      </span>
    </h2>
    <div class="blurb">
      <p>Lorem ipsum dolor sit amet, consectetur adipiscing elit, sed do eiusmod tempor incididunt ut labore et dolore magna aliqua. Quis ipsum suspendisse ultrices gravida. Risus commodo viverra maecenas accumsan lacus vel facilisis. Lorem ipsum dolor sit amet, consectetur adipiscing elit, sed do eiusmod tempor incididunt ut labore et dolore magna aliqua. Quis ipsum suspendisse ultrices gravida. Risus commodo viverra maecenas accumsan lacus vel facilisis. Lorem ipsum dolor sit amet, consectetur adipiscing elit, sed do eiusmod tempor incididunt ut labore et dolore magna aliqua. Quis ipsum suspendisse ultrices gravida. Risus commodo viverra maecenas accumsan lacus vel facilisis.</p>
      <p>Lorem ipsum dolor sit amet, consectetur adipiscing elit, sed do eiusmod tempor incididunt ut labore et dolore magna aliqua. Quis ipsum suspendisse ultrices gravida. Risus commodo viverra maecenas accumsan lacus vel facilisis. Lorem ipsum dolor sit amet, consectetur adipiscing elit, sed do eiusmod tempor incididunt ut labore et dolore magna aliqua. Quis ipsum suspendisse ultrices gravida. Risus commodo viverra maecenas accumsan lacus vel facilisis. Lorem ipsum dolor sit amet, consectetur adipiscing elit, sed do eiusmod tempor incididunt ut labore et dolore magna aliqua. Quis ipsum suspendisse ultrices gravida. Risus commodo viverra maecenas accumsan lacus vel facilisis.</p>
    </div>
  </section>

  <section class="spine">
    <div class="spine-text">
      <span class="word-italic glitch-sm">BLOOM</span>
      <span class="word-script">where you</span>
      <span class="word-block">STAND</span>
      <span class="spine-author">MARA ELLISON</span>
    </div>
  </section>

  <section class="front">
    <h1 class="front-title">
      <span class="word-italic glitch">BLOOM</span>
      <span class="word-script">where you</span>
      <span class="word-block">STAND</span>
    </h1>
    <p class="tagline">Discover 10 practical ways to<br>replace negative thoughts with knowing<br>the voice of God</p>
    <p class="author">MARA ELLISON</p>
  </section>
</main>
</body>
</html>
```